Beachfront Resort Landing Page

I need a design for a landing page related to a Beachfront Costa Rican Resort. This will be used as a Social Media landing page, so conversion is a must. Prefer someone with experience designing single-landing pages for conversions.

Can use this site as a reference for content / info - ramasolvento.com

The landing page needs to contain these items

"Book a 4 night Stay During the Costa Rican Green-Season, and get your 5th night Free at this All Inclusive Luxury Beachfront Resort!"

"As a Bonus, we'll throw in any of these Activities or Tours for Free! Don't wait! These will fill up fast."
"Free Massage"
"Night Hike"
"Birdwatching Tour"
"Max 2 per booking, can mix-match. While supplies last. Must redeemed during this stay" (in small print under text / images)

Also highlight these items too please

"Accessible only via boat, this Costa Rican Luxury Paradise is perfect for those wanting to escape the crowds, enjoy amazing cuisine, while swimming in our beachfront pool, and more"

"Green Season is known for whale migrations, enjoy watching the marine life from our beachfront location, or up close and personal via kayak or paddleboard"

"Paddleboards, kayaks, snorkeling gear, and more are free during your stay."

"Enjoy fresh cuisine and unique beverages daily"

"Nubeway Internet Access Included with all Bookings"

The landing page must have
- A contact form close to above the fold area
- Booking dates function around the same area
- CTA's related to most of whats mentioned above
- Can use images from the real site - ramasolvento.com
- Areas for videos on the landing page
- Must resemble a good landing page design for conversion, not a standard web-page. Those who know, will know.

Please let me know if you have any questions.

```html
<!DOCTYPE html>
<html lang="en">
<head>
<meta charset="utf-8">
<title>Casa Verdemar – Beachfront Costa Rican Resort</title>
<link rel="stylesheet" href="https://fonts.googleapis.com/css2?family=Poppins:wght@400;500;600;700;800&display=swap">
<style>
:root{
  --green:#4b5f46;
  --green-dark:#3f5239;
  --ink:#1f1f1f;
  --muted:#444;
  --soft:#f5f5f5;
  --white:#ffffff;
  --line:#c9c9c9;
}
*{box-sizing:border-box;margin:0;padding:0}
html,body{width:1200px;height:4910px;overflow:hidden}
body{position:relative;background:var(--white);font-family:"Poppins",sans-serif;color:var(--ink)}
.abs{position:absolute}
.photo{position:absolute}

/* hero */
.hero{left:0;top:0;width:1200px;height:711px;background:linear-gradient(180deg,#6c7f8e 0%,#b48a5e 30%,#7b5a33 55%,#5b6b64 75%,#a39b86 100%)}
.brand{position:absolute;left:110px;top:50px;display:flex;align-items:center;gap:10px;color:var(--white);font-weight:500;font-size:22px;letter-spacing:.5px}
.brand-dot{width:16px;height:16px;border-radius:50%;background:var(--white)}
.btn{position:absolute;display:flex;align-items:center;justify-content:center;border-radius:30px;font-weight:500;text-transform:uppercase}
.btn-light{background:var(--white);color:var(--ink)}
.btn-green{background:var(--green);color:var(--white)}
.btn-res{left:916px;top:25px;width:172px;height:57px;font-size:16px}
.hero-title{position:absolute;left:108px;top:232px;color:var(--white);font-weight:800;font-size:60px;line-height:70px;text-transform:uppercase}

.contact{left:655px;top:135px;width:433px;height:467px;background:rgba(75,95,70,.92);border-radius:8px}
.contact h2{position:absolute;left:0;top:22px;width:100%;text-align:center;color:var(--white);font-size:23px;font-weight:600}
.field{position:absolute;border:1px solid rgba(255,255,255,.75);color:var(--white);font-size:15px;padding:12px 12px}
.btn-submit{left:158px;top:391px;width:119px;height:53px;font-size:16px}

/* reservation card */
.booking{left:112px;top:640px;width:976px;height:347px;background:var(--white);box-shadow:0 2px 12px rgba(0,0,0,.08)}
.booking h2{position:absolute;left:32px;top:30px;font-size:28px;font-weight:500}
.step-line{position:absolute;top:115px;left:61px;width:574px;height:2px;background:var(--line)}
.step{position:absolute;top:88px;width:54px;height:54px;border-radius:50%;background:#7a7a7a;color:var(--white);display:flex;align-items:center;justify-content:center;font-size:22px}
.step.on{background:var(--green)}
.step-label{position:absolute;top:150px;width:200px;text-align:center;font-size:16px}
.sel-title{position:absolute;left:36px;top:198px;font-size:17px;font-weight:600}
.in-label{position:absolute;top:232px;font-size:14px;color:var(--muted)}
.input{position:absolute;top:263px;height:46px;border:1px solid #8a8a8a}
.input svg{position:absolute;right:12px;top:14px}
.btn-search{left:802px;top:257px;width:134px;height:57px;font-size:18px}

/* promo */
.band-soft{left:0;top:711px;width:1200px;height:912px;background:var(--soft);z-index:-1}
.promo-card{left:634px;top:1095px;width:454px;height:393px;background:var(--white);box-shadow:0 2px 12px rgba(0,0,0,.06)}
.promo-card p{position:absolute;left:38px;top:48px;width:400px;font-size:26px;line-height:39px;font-weight:500}
.btn-book{left:35px;top:275px;width:169px;height:63px;font-size:18px}

/* all inclusive */
.section-title{position:absolute;left:0;width:1200px;text-align:center;font-size:37px;font-weight:600;text-transform:uppercase}
.caption{position:absolute;text-align:center;font-size:17px;line-height:27px;color:var(--ink)}

/* videos */
.band-videos{left:0;top:2610px;width:1200px;height:613px;background:var(--soft)}
.play{position:absolute;border-radius:50%;display:flex;align-items:center;justify-content:center}

/* features */
.quote{position:absolute;border-left:6px solid var(--green);padding-left:22px;font-size:17px;line-height:25px;color:var(--ink)}

/* footer */
.footer{left:0;top:4582px;width:1200px;height:328px;background:var(--green);color:var(--white)}
.footer .brand{left:0;top:100px;width:1200px;justify-content:center;font-size:28px}
.footer .brand-dot{width:22px;height:22px}
.copy{position:absolute;left:0;top:188px;width:1200px;text-align:center;font-size:16px}
.social{position:absolute;top:237px;width:38px;height:38px;border:2px solid var(--white);border-radius:50%}
</style>
</head>
<body>

<section class="abs hero">
  <div class="photo" role="img" aria-label="Sunset over a rocky jungle coastline with waves rolling onto the beach" style="inset:0;background:linear-gradient(180deg,rgba(90,110,130,.4),rgba(0,0,0,0) 40%,rgba(30,50,40,.3))"></div>
  <div class="brand"><span class="brand-dot"></span>CASA VERDEMAR</div>
  <div class="btn btn-light btn-res">Reservations</div>
  <h1 class="hero-title">Beachfront<br>Costa Rican<br>Resort</h1>

  <form class="abs contact">
    <h2>CONTACT US</h2>
    <div class="field" style="left:27px;top:78px;width:381px;height:48px">Full Name *</div>
    <div class="field" style="left:27px;top:137px;width:183px;height:50px">Email *</div>
    <div class="field" style="left:223px;top:137px;width:185px;height:50px">Phone Number *</div>
    <div class="field" style="left:27px;top:200px;width:381px;height:48px">Subject *</div>
    <div class="field" style="left:27px;top:261px;width:381px;height:107px">Comment or Message *</div>
    <div class="btn btn-light btn-submit">Submit</div>
  </form>
</section>

<div class="abs band-soft"></div>

<section class="abs booking">
  <h2>RESERVATIONS</h2>
  <div class="step-line"></div>
  <div class="step on" style="left:34px">1</div>
  <div class="step" style="left:213px">2</div>
  <div class="step" style="left:412px">3</div>
  <div class="step" style="left:608px">4</div>
  <div class="step-label" style="left:-39px">Dates</div>
  <div class="step-label" style="left:140px">Accommodations</div>
  <div class="step-label" style="left:339px">Enhancements</div>
  <div class="step-label" style="left:535px">Confirmation</div>
  <div class="sel-title">Your Selections</div>
  <div class="in-label" style="left:36px">Check-in</div>
  <div class="in-label" style="left:284px">Check-out</div>
  <div class="in-label" style="left:533px">No of Guest</div>
  <div class="input" style="left:37px;width:238px"><svg width="18" height="18" viewBox="0 0 18 18"><rect x="1" y="3" width="16" height="14" fill="none" stroke="#777" stroke-width="1.5"/><line x1="1" y1="7" x2="17" y2="7" stroke="#777" stroke-width="1.5"/><line x1="5" y1="1" x2="5" y2="5" stroke="#777" stroke-width="1.5"/><line x1="13" y1="1" x2="13" y2="5" stroke="#777" stroke-width="1.5"/></svg></div>
  <div class="input" style="left:284px;width:238px"><svg width="18" height="18" viewBox="0 0 18 18"><rect x="1" y="3" width="16" height="14" fill="none" stroke="#777" stroke-width="1.5"/><line x1="1" y1="7" x2="17" y2="7" stroke="#777" stroke-width="1.5"/><line x1="5" y1="1" x2="5" y2="5" stroke="#777" stroke-width="1.5"/><line x1="13" y1="1" x2="13" y2="5" stroke="#777" stroke-width="1.5"/></svg></div>
  <div class="input" style="left:534px;width:238px"><svg width="14" height="18" viewBox="0 0 14 18"><path d="M2 7 L7 12 L12 7 Z" fill="#555"/></svg></div>
  <div class="btn btn-green btn-search">Search</div>
</section>

<div class="photo" role="img" aria-label="Thatched jungle bungalow on stilts surrounded by lush tropical plants" style="left:112px;top:1055px;width:570px;height:475px;background:linear-gradient(160deg,#3f6a2c,#6f8f3e 45%,#8a6a3e 60%,#2f5a22)"></div>
<section class="abs promo-card">
  <p>Book a 4 night Stay During the Costa Rican Green-Season, and get your 5th night Free at this All Inclusive Luxury Beachfront Resort!"</p>
  <div class="btn btn-green btn-book">Book Now</div>
</section>

<h2 class="section-title" style="top:1685px">An All-Inclusive Stay</h2>
<div class="photo" role="img" aria-label="Guest relaxing during a massage on the beach" style="left:112px;top:1775px;width:311px;height:280px;background:linear-gradient(180deg,#2f5a2c,#5a8a9a 40%,#c89a80 70%,#e9e4dc)"></div>
<div class="photo" role="img" aria-label="Colourful toucan perched in the rainforest" style="left:444px;top:1775px;width:312px;height:280px;background:linear-gradient(135deg,#2a4a1e,#4f7a30 50%,#1a2e14)"></div>
<div class="photo" role="img" aria-label="Red-eyed tree frog on a branch at night" style="left:777px;top:1775px;width:311px;height:280px;background:radial-gradient(circle at 50% 50%,#6f9a30,#1c2a10 65%,#0a0f06)"></div>
<div class="caption" style="left:112px;top:2076px;width:311px">Free Massage</div>
<div class="caption" style="left:444px;top:2076px;width:312px">Birdwatching Tour</div>
<div class="caption" style="left:777px;top:2076px;width:311px">Night Hike</div>

<div class="photo" role="img" aria-label="Horseback ride along the shoreline" style="left:278px;top:2145px;width:311px;height:280px;background:linear-gradient(180deg,#9ab4c4,#5f8da0 45%,#8a7560 70%,#b89a78)"></div>
<div class="photo" role="img" aria-label="Candlelit dinner table set by the ocean under palm trees" style="left:610px;top:2145px;width:312px;height:280px;background:linear-gradient(180deg,#4c6a2c,#3a8ab0 50%,#6a6a70 75%,#3a3a40)"></div>
<div class="caption" style="left:283px;top:2445px;width:301px">As a Bonus, we'll throw in any of these Activities or Tours for Free! Don't wait! These will fill up fast.</div>
<div class="caption" style="left:615px;top:2445px;width:302px">Max 2 per booking, can mix-match. While supplies last. Must redeemed during this stay</div>

<section class="abs band-videos">
  <h2 class="section-title" style="top:75px">Our Videos</h2>
  <div class="photo" role="img" aria-label="Video thumbnail: aerial view of the jungle coastline" style="left:0;top:204px;width:301px;height:253px;background:linear-gradient(135deg,#c9d4cf,#a8b8a4 50%,#b8c8c4);opacity:.85">
    <div class="play" style="left:80px;top:104px;width:46px;height:46px;background:rgba(120,120,120,.6)"><svg width="18" height="20" viewBox="0 0 18 20"><path d="M2 1 L17 10 L2 19 Z" fill="#fff"/></svg></div>
  </div>
  <div class="photo" role="img" aria-label="Video thumbnail: resort bungalow among palms" style="left:930px;top:204px;width:270px;height:253px;background:linear-gradient(135deg,#b9c2b0,#a4ac94 50%,#c4c8bc);opacity:.85">
    <div class="play" style="left:170px;top:104px;width:46px;height:46px;background:rgba(120,120,120,.6)"><svg width="18" height="20" viewBox="0 0 18 20"><path d="M2 1 L17 10 L2 19 Z" fill="#fff"/></svg></div>
  </div>
  <div class="photo" role="img" aria-label="Video thumbnail: beachfront infinity pool surrounded by jungle" style="left:339px;top:158px;width:553px;height:368px;background:linear-gradient(180deg,#3e6a30,#6a8a5a 35%,#3ab0c4 60%,#7acbd4 85%,#5a6a70);box-shadow:0 4px 14px rgba(0,0,0,.15)">
    <div class="play" style="left:242px;top:152px;width:68px;height:68px;background:#111"><svg width="24" height="28" viewBox="0 0 24 28"><path d="M3 1 L23 14 L3 27 Z" fill="#fff"/></svg></div>
  </div>
</section>

<p class="quote" style="left:112px;top:3298px;width:410px">Accessible only via boat, this Costa Rican Luxury Paradise is perfect for those wanting to escape the crowds, enjoy amazing cuisine, while swimming in our beachfront pool, and more"</p>
<p class="quote" style="left:623px;top:3298px;width:400px">Green Season is known for whale migrations, enjoy watching the marine life from our beachfront location, or up close and personal via kayak or paddleboard</p>
<div class="photo" role="img" aria-label="Small boat cruising along a jungle river" style="left:112px;top:3458px;width:465px;height:440px;background:linear-gradient(180deg,#6a9a3a,#3f6a2a 40%,#4a5a30 70%,#2a3a1e)"></div>
<div class="photo" role="img" aria-label="Dolphins swimming off the forested coast" style="left:623px;top:3458px;width:465px;height:440px;background:linear-gradient(180deg,#d4dee4,#3f6a3a 25%,#2f5a2a 45%,#2a6a9a 60%,#3a7ab0)"></div>

<p class="quote" style="left:112px;top:3962px;width:410px">Paddleboards, kayaks, snorkeling gear, and more are free during your stay.</p>
<p class="quote" style="left:623px;top:3962px;width:320px">Enjoy fresh cuisine and unique beverages daily</p>
<div class="photo" role="img" aria-label="Couple paddling a red kayak near the rocky shore" style="left:112px;top:4044px;width:465px;height:440px;background:linear-gradient(180deg,#3a5a2a,#4a6a4a 30%,#5a9ac4 55%,#7ab0d4)"></div>
<div class="photo" role="img" aria-label="Plates of fresh food and drinks on a wooden table" style="left:623px;top:4044px;width:465px;height:440px;background:radial-gradient(circle at 45% 55%,#d8c8b0,#8a5a30 55%,#4a2a14)"></div>

<footer class="abs footer">
  <div class="brand"><span class="brand-dot"></span>CASA VERDEMAR</div>
  <p class="copy">Copyright © 2024 Casa Verdemar. All rights reserved.</p>
  <span class="social" style="left:474px"></span>
  <span class="social" style="left:517px"></span>
  <span class="social" style="left:560px"></span>
  <span class="social" style="left:603px"></span>
  <span class="social" style="left:646px"></span>
  <span class="social" style="left:689px"></span>
</footer>

</body>
</html>
```